Need a Modern WIX Website design

Need help designing a modern WIX website. I already started building on studio.plovex.com but I am not a designer and would like a more modern, update aesthetic look. This is not an e-commerce site. Just a website portraying our company, posting what products we offer, contact, about us, services. Logo is already on the studio.plovex version with some content. Need a designer with vision, and ingenuity to set it apart change it a little and make it stand out. Please look at the current site for redesign and/or ideas https://norvatradeco.plovexsite.com/website
also need the design to be connected to our google domain www.nvt.trade

Please feel free to ask as many questions as possible

Target Market(s)

Tire repair shops, Tire stores, mechanic shops, tire replacement franchises, wheel and rim stores

Industry/Entity Type

we are wholesalers, B2B ..sell tire repair materials, tire hand tools, machinery, chemicals, wheel lug nuts, wheel accessories

Coding

Coded - Design and coding required

Number of Pages Required

5+ page

Font styles to use
Other font styles liked:
• Let designer choose

Colors

Designer to choose colors to be used in the design.

Requirements
Must have
• modern design layout, videos, high quality pictures, different ideas for pages (Home, shop, about, products, services, contact, faq, meet the team) translatable english to spanish
Nice to have
• would like to have an up to date modern look, interactive, easy to navigate,
Should not have
• not be hard to navigate for our customers

```html
<!DOCTYPE html>
<html lang="en">
<head>
<meta charset="UTF-8">
<title>Norva Trade Co — Specializing in Tire Solutions</title>
<link rel="stylesheet" href="https://fonts.googleapis.com/css2?family=Oswald:wght@400;500;600;700&family=Poppins:wght@400;500;600&display=swap">
<style>
:root{
  --bg:#1b1b1d;
  --bg-deep:#141416;
  --card:#2a2a2c;
  --red:#e0262c;
  --red-dark:#7a1016;
  --white:#ffffff;
  --muted:#a9a9ad;
  --light-card:#eeeeee;
  --grey:#8a8a8e;
}
*{margin:0;padding:0;box-sizing:border-box}
html,body{width:1200px;height:4391px;overflow:hidden;background:var(--bg);color:var(--white);font-family:"Poppins",sans-serif}
.page{position:relative;width:1200px;height:4391px;overflow:hidden}
.abs{position:absolute}
.heading{font-family:"Oswald",sans-serif;font-weight:600;text-transform:uppercase;letter-spacing:.5px}

/* header */
.site-header{position:absolute;left:0;top:0;width:1200px;height:85px;background:var(--bg-deep);z-index:5}
.brand{position:absolute;left:89px;top:16px;display:flex;align-items:center;gap:10px}
.brand-mark{width:44px;height:44px;border:3px solid var(--red)}
.brand-name{font-family:"Oswald",sans-serif;font-weight:600;font-size:30px;line-height:1;color:var(--white);text-transform:uppercase}
.brand-tag{font-family:"Oswald",sans-serif;font-weight:600;font-size:9px;letter-spacing:2px;color:var(--white);text-transform:uppercase;margin-top:4px}
.nav{position:absolute;left:425px;top:34px;display:flex;gap:22px;font-size:12px;font-weight:500;text-transform:uppercase}
.nav a{color:var(--white);text-decoration:none}
.call{position:absolute;left:952px;top:26px;display:flex;align-items:center;gap:10px}
.call small{display:block;font-size:9px;color:var(--muted);font-weight:600}
.call strong{display:block;font-size:16px;font-weight:600}

/* hero */
.hero-photo{position:absolute;left:0;top:85px;width:1200px;height:835px;background:linear-gradient(115deg,#26262a 0%,#3c3c42 30%,#7a6a66 52%,#c2472e 68%,#d86a3a 76%,#6e6e74 100%)}
.hero-frame{position:absolute;left:89px;top:270px;width:312px;height:395px;border:14px solid var(--red);border-right:none}
.hero-frame::before,.hero-frame::after{content:"";position:absolute;right:-14px;width:14px;height:70px;background:var(--red)}
.hero-frame::before{top:-14px}.hero-frame::after{bottom:-14px}
.hero-title{position:absolute;left:148px;top:372px;font-family:"Oswald",sans-serif;font-weight:700;font-size:72px;line-height:76px;text-transform:uppercase}
.hero-rule{position:absolute;left:150px;top:356px;width:62px;height:4px;background:#777}
.hero-sub{position:absolute;left:148px;top:535px;font-family:"Oswald",sans-serif;font-size:22px;text-transform:uppercase}

/* about */
.about-photo{position:absolute;left:205px;top:972px;width:378px;height:516px;background:linear-gradient(160deg,#c4c6c9 0%,#a3a5a9 45%,#8a5a5c 75%,#8d8f93 100%)}
.dots{position:absolute;left:147px;top:1418px;width:125px;height:120px;background-image:radial-gradient(#555 2px,transparent 2.5px);background-size:15px 15px}
.about-title{position:absolute;left:660px;top:1044px;font-size:42px}
.about-sub{position:absolute;left:660px;top:1098px;font-family:"Oswald",sans-serif;font-size:14px;text-transform:uppercase}
.about-text{position:absolute;left:660px;top:1147px;width:395px;font-size:12.5px;line-height:20.5px;color:var(--muted)}
.about-text p+p{margin-top:10px}
.btn{position:absolute;display:inline-block;background:var(--red);color:var(--white);font-size:11px;font-weight:600;text-transform:uppercase;text-align:center}

/* section headings */
.sec-title{position:absolute;left:0;width:1200px;text-align:center;font-size:42px}
.sec-sub{position:absolute;left:0;width:1200px;text-align:center;font-family:"Oswald",sans-serif;font-size:13px;text-transform:uppercase}
.sec-rule{position:absolute;left:565px;width:70px;height:2px;background:#555}

/* products */
.arrow-btn{position:absolute;top:1597px;width:32px;height:34px;display:flex;align-items:center;justify-content:center;font-size:14px}
.product{position:absolute;top:1693px;width:186px;height:259px;background:var(--light-card)}
.product .shot{position:absolute;left:20px;top:16px;width:146px;height:150px;background:linear-gradient(180deg,#eeeeee,#dedede)}
.product p{position:absolute;left:27px;top:184px;width:140px;font-family:"Oswald",sans-serif;font-size:11px;line-height:17px;color:#333;text-transform:uppercase}

/* values */
.values-band{position:absolute;left:0;top:2020px;width:1200px;height:540px;clip-path:polygon(0 18px,100% 0,100% 470px,0 100%);background:linear-gradient(90deg,#3a0e12 0%,#261618 35%,#1c1c20 62%,#3a1416 82%,#6a1a1c 100%)}
.value{position:absolute;top:2170px;width:170px;text-align:center}
.value svg{display:block;margin:0 auto}
.value h3{margin-top:18px;font-size:16px}
.value p{margin-top:10px;font-size:12px;line-height:18px;color:var(--muted)}

/* services */
.service{position:absolute;top:2727px;width:302px;height:409px;background:var(--card)}
.service .shot{height:240px}
.service h3{position:absolute;left:35px;top:273px;font-size:16px}
.service p{position:absolute;left:35px;top:305px;width:235px;font-size:11.5px;line-height:18px;color:var(--muted)}
.service a{position:absolute;left:35px;top:370px;font-size:12px;font-weight:600;color:var(--red);text-decoration:none;text-transform:uppercase}

/* brands */
.partner{position:absolute;top:3340px;width:130px;text-align:center}
.partner .badge{width:80px;height:80px;margin:0 auto;border:2px solid #6a6a6e;border-radius:50%}
.partner span{display:block;margin-top:20px;font-family:"Oswald",sans-serif;font-size:12px;text-transform:uppercase}

/* map */
.map{position:absolute;left:179px;top:3549px;width:839px;height:354px;background:linear-gradient(135deg,#6c6e74,#55575d)}
.map-tabs{position:absolute;left:10px;top:10px;display:flex;background:#fff;font-size:15px;color:#333}
.map-tabs span{padding:8px 16px}
.map-tabs span+span{color:#777}
.map-zoom{position:absolute;right:18px;top:280px;width:36px;height:62px;background:#fff;color:#555;font-size:24px;text-align:center;line-height:30px}

/* footer */
.footer-glow{position:absolute;left:0;top:3700px;width:1200px;height:691px;background:linear-gradient(165deg,transparent 20%,#2c1416 55%,#4c1216 100%);clip-path:polygon(0 30%,100% 0,100% 100%,0 100%)}
.footer-brand{position:absolute;left:99px;top:4062px;display:flex;align-items:center;gap:10px}
.social{position:absolute;top:4152px;width:42px;height:42px;border-radius:50%;background:#2f2f33}
.foot-col h4{font-size:17px}
.foot-col{position:absolute;top:4012px}
.foot-col a,.foot-col li{display:block;color:var(--white);text-decoration:none;font-size:12px;line-height:31px;list-style:none}
.contact-item{display:flex;gap:10px;font-size:12px;line-height:17px;margin-top:18px}
.newsletter p{font-size:12px;line-height:19px;margin-top:20px;width:230px}
.subscribe{margin-top:20px;width:263px;height:48px;background:#fff;display:flex;align-items:center;justify-content:space-between;padding:0 16px;color:#888;font-size:12px}
.foot-rule{position:absolute;left:90px;top:4330px;width:1020px;height:1px;background:#3c3c40}
.copyright{position:absolute;left:0;top:4352px;width:1200px;text-align:center;font-size:11px;font-weight:600;text-transform:uppercase}
.chat{position:absolute;left:1127px;top:4300px;width:58px;height:58px;border-radius:50%;background:var(--red);display:flex;align-items:center;justify-content:center}
</style>
</head>
<body>
<div class="page">

  <header class="site-header">
    <div class="brand">
      <div class="brand-mark"></div>
      <div>
        <div class="brand-name">Norva Trade Co</div>
        <div class="brand-tag">Specializing in tire solutions</div>
      </div>
    </div>
    <nav class="nav">
      <svg width="16" height="14" viewBox="0 0 16 14"><path d="M8 0L0 7h2v7h4V9h4v5h4V7h2z" fill="#e0262c"/></svg>
      <a href="#">Shop</a><a href="#">About</a><a href="#">Products</a><a href="#">Services</a><a href="#">Contact</a><a href="#">FAQ</a><a href="#">Team</a>
    </nav>
    <div class="call">
      <svg width="32" height="32" viewBox="0 0 32 32"><circle cx="16" cy="16" r="16" fill="#e0262c"/><path d="M11 9c1-1 2 0 3 2s0 2-1 3c1 2 2 3 4 4 1-1 1-2 3-1s3 2 2 3c-1 2-3 2-5 1-3-2-5-4-7-7-1-2-1-4 1-5z" fill="#fff"/></svg>
      <div><small>CALL US:</small><strong>833-555-0182</strong></div>
    </div>
  </header>

  <div class="hero-photo" role="img" aria-label="Mechanic fitting a tire onto a car wheel in a workshop, lit with warm red light"></div>
  <svg class="abs" style="left:0;top:680px" width="1200" height="240"><polygon points="0,160 1200,40 1200,240 0,240" fill="#1b1b1d"/></svg>
  <div class="hero-frame"></div>
  <div class="hero-rule"></div>
  <h1 class="hero-title">Norva Trade<br>Company</h1>
  <div class="hero-sub">Specializing in tire solutions</div>
  <svg class="abs" style="left:978px;top:705px" width="130" height="130"><circle cx="65" cy="65" r="65" fill="#8d8d91"/><polygon points="56,53 56,78 78,65" fill="#fff"/></svg>

  <div class="dots"></div>
  <div class="about-photo" role="img" aria-label="Rows of silver alloy wheels displayed on red wall racks"></div>
  <h2 class="heading about-title">About NVT</h2>
  <div class="about-sub">Your one stop tire repair supplier in New York</div>
  <div class="about-text">
    <p>At Norva Trade Co we make sure to offer our clients the best</p>
    <p>Selection of tire repair products, tools and machinery as well as provide them with superb customer service. Our staff works with our customers to find exactly the right part they need for the right price. We're here to help inform you about our products, so that you only buy what is absolutely necessary for your establishment. Contact us today to learn more about what we do.</p>
  </div>
  <a class="btn" style="left:660px;top:1365px;width:142px;height:38px;line-height:38px">Find out more</a>

  <h2 class="heading sec-title" style="top:1570px">Products</h2>
  <div class="sec-sub" style="top:1627px">Supplying the best quality merchandise</div>
  <div class="sec-rule" style="top:1656px"></div>
  <div class="arrow-btn" style="left:1020px;background:#77777b">‹</div>
  <div class="arrow-btn" style="left:1059px;background:var(--red)">›</div>

  <div class="product" style="left:109px"><div class="shot" role="img" aria-label="Black rubber snap-in valve stem"></div><p>100- Valve alligator rubber snap-in, TR 413</p></div>
  <div class="product" style="left:307px"><div class="shot" role="img" aria-label="Digital tire inflator with red hose and pistol grip"></div><p>Pro digital tire inflator pressure pistol grip gauge</p></div>
  <div class="product" style="left:506px"><div class="shot" role="img" aria-label="Chrome bulge acorn lug nuts"></div><p>Lug nut - bulge acorn (3/4) - M12 1.5 (2 pc)</p></div>
  <div class="product" style="left:705px"><div class="shot" role="img" aria-label="Can of cold vulcanizing fluid with brush top"></div><p>203-F cold vulcanizing fluid (flammable), with brush top</p></div>
  <div class="product" style="left:903px"><div class="shot" role="img" aria-label="Black thin wall impact flip socket"></div><p>1/2-inch drive 6-point thin wall impact flip socket, 19mm x 21mm</p></div>

  <div class="values-band" role="img" aria-label="Dark red backdrop with a red car at right and a wheel at lower left"></div>

  <div class="value" style="left:60px">
    <svg width="80" height="80" viewBox="0 0 80 80" fill="none" stroke="#ccc" stroke-width="2"><rect x="10" y="8" width="36" height="48"/><path d="M18 20h20M18 30h20M18 40h12"/><path d="M34 60l14-14 10 10 14-14" stroke="#e0262c" stroke-width="3"/></svg>
    <h3 class="heading">Commitment</h3><p>We understand, respect and value our...</p>
  </div>
  <div class="value" style="left:232px">
    <svg width="80" height="80" viewBox="0 0 80 80" fill="none" stroke="#ccc" stroke-width="2"><circle cx="40" cy="40" r="30"/><path d="M32 30a8 8 0 1116 0c0 6-5 8-5 14h-6c0-6-5-8-5-14z" stroke="#e0262c" stroke-width="3"/><path d="M36 50h8M37 55h6"/></svg>
    <h3 class="heading">Innovation</h3><p>We keep innovating to improve the...</p>
  </div>
  <div class="value" style="left:404px">
    <svg width="80" height="80" viewBox="0 0 80 80" fill="none" stroke="#ccc" stroke-width="2"><circle cx="40" cy="14" r="9"/><path d="M35 14l4 4 6-7"/><ellipse cx="40" cy="46" rx="32" ry="20"/><rect x="18" y="38" width="44" height="16" stroke="#e0262c" stroke-width="2.5"/></svg>
    <h3 class="heading">Simplicity</h3><p>We get things done simply and flexibly.</p>
  </div>
  <div class="value" style="left:576px">
    <svg width="80" height="80" viewBox="0 0 80 80" fill="none" stroke="#ccc" stroke-width="2"><polygon points="40,6 48,14 60,12 62,24 72,32 66,44 70,56 58,60 52,72 40,66 28,72 22,60 10,56 14,44 8,32 18,24 20,12 32,14"/><circle cx="40" cy="38" r="14"/><polygon points="40,30 43,36 49,37 44,41 46,47 40,44 34,47 36,41 31,37 37,36" stroke="#e0262c"/></svg>
    <h3 class="heading">Excellence</h3><p>We achieve high quality in everything we do...</p>
  </div>
  <div class="value" style="left:748px">
    <svg width="80" height="80" viewBox="0 0 80 80" fill="none" stroke="#ccc" stroke-width="2"><rect x="8" y="16" width="64" height="48"/><path d="M18 56V44M30 56V38M42 56V42M54 56V30"/><path d="M16 36l14-10 12 6 18-14" stroke="#e0262c" stroke-width="3"/><circle cx="16" cy="10" r="6" stroke="#e0262c"/></svg>
    <h3 class="heading">Proactivity</h3><p>We resolve problems as quick as possible...</p>
  </div>

  <h2 class="heading sec-title" style="top:2603px">Services offered</h2>
  <div class="sec-sub" style="top:2660px">Satisfying our clients</div>
  <div class="sec-rule" style="top:2690px"></div>

  <article class="service" style="left:133px">
    <div class="shot" role="img" aria-label="Gloved hands holding a new tire" style="background:linear-gradient(160deg,#4a6884 0%,#3a3c42 55%,#55504c 100%)"></div>
    <h3 class="heading">Stellar customer service</h3>
    <p>For over 25 years, we have been providing excellent customer service by going the extra mile...</p>
    <a href="#">Learn more</a>
  </article>
  <article class="service" style="left:449px">
    <div class="shot" role="img" aria-label="Row of new tires in a smoky showroom" style="background:linear-gradient(180deg,#6a6c70 0%,#2a2b2e 60%,#1c1d20 100%)"></div>
    <h3 class="heading">High quality products</h3>
    <p>Our products are trusted for their design &amp; engineering, &amp; we will continue to equip our customers...</p>
    <a href="#">Learn more</a>
  </article>
  <article class="service" style="left:765px">
    <div class="shot" role="img" aria-label="Mechanic using an impact wrench on a car wheel" style="background:linear-gradient(160deg,#3e5676 0%,#5e6066 55%,#7a3a36 100%)"></div>
    <h3 class="heading">Commitment</h3>
    <p>When a customer comes to us for parts it is often in the context of a long project. We offer Tire Alignment...</p>
    <a href="#">Learn more</a>
  </article>

  <h2 class="heading sec-title" style="top:3217px">Our brands</h2>
  <div class="sec-sub" style="top:3273px">Who we work with</div>
  <div class="sec-rule" style="top:3303px"></div>
  <div class="partner" style="left:78px"><div class="badge"></div><span>Keystone Rubber</span></div>
  <div class="partner" style="left:209px"><div class="badge"></div><span>Delta Bond</span></div>
  <div class="partner" style="left:341px"><div class="badge"></div><span>Corvan Industries</span></div>
  <div class="partner" style="left:474px"><div class="badge"></div><span>Ironleaf Tools</span></div>
  <div class="partner" style="left:605px"><div class="badge"></div><span>Brightcoat Labs</span></div>
  <div class="partner" style="left:738px"><div class="badge"></div><span>Tredmark</span></div>
  <div class="partner" style="left:869px"><div class="badge"></div><span>Patchwell Pro</span></div>
  <div class="partner" style="left:1002px"><div class="badge"></div><span>Halden Works</span></div>

  <div class="footer-glow"></div>

  <div class="map" role="img" aria-label="Street map showing the company location">
    <div class="map-tabs"><span>Map</span><span>Satellite</span></div>
    <div class="map-zoom">+<br>−</div>
  </div>

  <div class="footer-brand">
    <div class="brand-mark" style="width:52px;height:52px"></div>
    <div>
      <div class="brand-name" style="font-size:36px">Norva Trade Co</div>
      <div class="brand-tag" style="font-size:10px">Specializing in tire solutions</div>
    </div>
  </div>
  <div class="social" style="left:132px"></div>
  <div class="social" style="left:184px"></div>
  <div class="social" style="left:236px"></div>
  <div class="social" style="left:288px"></div>

  <div class="foot-col" style="left:433px">
    <h4 class="heading">Quick links</h4>
    <ul style="margin-top:8px"><li>Shop</li><li>About Us</li><li>Our Products</li><li>Our Services</li><li>Faq</li><li>Team</li></ul>
  </div>
  <div class="foot-col" style="left:590px">
    <h4 class="heading">Contact info</h4>
    <div class="contact-item"><svg width="12" height="10" viewBox="0 0 12 10"><rect width="12" height="10" fill="#e0262c"/><path d="M0 0l6 5 6-5" stroke="#fff" fill="none"/></svg><div>Email:<br>hello@norvatradeco.com</div></div>
    <div class="contact-item"><svg width="12" height="12" viewBox="0 0 12 12"><path d="M2 1c1-1 2 0 3 2 0 1-1 1-1 2 1 1 2 2 3 2 1-1 1-1 2-1 2 1 2 2 1 3-3 2-9-3-8-8z" fill="#e0262c"/></svg><div>Phone:<br>833-555-0182</div></div>
    <div class="contact-item"><svg width="12" height="14" viewBox="0 0 12 14"><path d="M6 0a6 6 0 00-6 6c0 4 6 8 6 8s6-4 6-8a6 6 0 00-6-6z" fill="#e0262c"/><circle cx="6" cy="6" r="2" fill="#1b1b1d"/></svg><div>Location:<br>218 Harbor Line Street Oakview,<br>CA 94610</div></div>
  </div>
  <div class="foot-col newsletter" style="left:847px">
    <h4 class="heading">Newsletter</h4>
    <p>Subscribe to our email address to get the latest news.</p>
    <div class="subscribe"><span>✉ Enter Your Email...</span><svg width="16" height="16" viewBox="0 0 16 16"><path d="M0 7L16 0 11 16 8 9z" fill="#e0262c"/></svg></div>
  </div>

  <div class="foot-rule"></div>
  <div class="copyright">©2022 by Norva Trade Co</div>
  <div class="chat"><svg width="30" height="26" viewBox="0 0 30 26"><path d="M4 2h22a3 3 0 013 3v12a3 3 0 01-3 3H12l-6 5v-5H4a3 3 0 01-3-3V5a3 3 0 013-3z" fill="#fff"/><circle cx="9" cy="11" r="2" fill="#e0262c"/><circle cx="15" cy="11" r="2" fill="#e0262c"/><circle cx="21" cy="11" r="2" fill="#e0262c"/></svg></div>

</div>
</body>
</html>
```